Infographic and content adjustment

For this project, the website content and the templates are already in place. We would need a professional placement of the content into the website, with appropriate and modern icons and/or high Res photos. The website "plenvoria.com" provides service to industry or social associations.

We like to see designs on below two templates to be able to compare. A template is already in place on
www.plenvoria.com/new

The second template would be:
www.plenvoria.com/new2

We would like to receive designs on both templates, so that we can choose the best.

The designer can use the attached power point content, revise the wording if needed and propose a professional design of those contents in the current template. High Res version of the pictures will be provided if necessary.

Target Market(s)

associations, their members,

Industry/Entity Type

Industry

Requirements
Must have
• easy and fast navigation, relevant icons and pictures, short and direct message.

```html
<!DOCTYPE html>
<html lang="en">
<head>
<meta charset="utf-8">
<title>Plenvoria</title>
<link href="https://fonts.googleapis.com/css2?family=Montserrat:wght@300;400&display=swap" rel="stylesheet">
<style>
  :root {
    --bar-teal: rgba(96, 186, 178, 0.82);
    --auth-teal: #3fa89f;
    --auth-text: #1f4c48;
    --menu-dark: #1f1f1f;
    --menu-teal: rgba(104, 190, 180, 0.88);
    --menu-active: #86e3d4;
    --white: #ffffff;
    --footer: #272324;
    --sky-top: #7f93a3;
    --sky-mid: #9aa7ae;
    --city-low: #5d6466;
  }
  * { box-sizing: border-box; margin: 0; padding: 0; }
  html, body { width: 1200px; height: 749px; overflow: hidden; }
  body {
    font-family: "Montserrat", Arial, sans-serif;
    color: var(--white);
    position: relative;
    background: var(--footer);
  }
  .hero-photo {
    position: absolute; left: 0; top: 0; width: 1200px; height: 686px;
    background: linear-gradient(180deg, var(--sky-top) 0%, var(--sky-mid) 45%, #878d8f 62%, var(--city-low) 100%);
  }
  .top-bar {
    position: absolute; left: 0; top: 0; width: 1200px; height: 65px;
    background: var(--bar-teal);
  }
  .brand {
    position: absolute; left: 75px; top: 9px;
    font-size: 42px; font-weight: 300; letter-spacing: 1px; line-height: 1;
    padding-top: 5px;
  }
  .auth {
    position: absolute; left: 770px; top: 0; width: 351px; height: 65px;
    background: var(--auth-teal); display: flex;
  }
  .auth a {
    flex: 1; display: flex; align-items: center; justify-content: center;
    color: var(--auth-text); text-decoration: none; font-size: 21px; letter-spacing: 1px;
  }
  .main-menu {
    position: absolute; left: 77px; top: 65px; width: 273px;
    border-top: 9px solid var(--menu-dark); list-style: none;
    background: var(--menu-teal);
  }
  .main-menu li {
    height: 42px; display: flex; align-items: center; justify-content: space-between;
    padding: 0 16px 0 27px; font-size: 20px; letter-spacing: 1px;
  }
  .main-menu li.active { background: var(--menu-active); }
  .tagline {
    position: absolute; right: 75px; top: 454px; text-align: right;
    font-size: 29px; font-weight: 300; line-height: 36px;
    text-shadow: 0 1px 3px rgba(0,0,0,0.35);
  }
  .tagline p + p { margin-top: 34px; }
  .site-footer {
    position: absolute; left: 0; top: 686px; width: 1200px; height: 63px;
    background: var(--footer);
  }
  .social { position: absolute; left: 0; top: 0; }
</style>
</head>
<body>
  <div class="hero-photo" role="img" aria-label="Aerial photo of a city skyline with a tall art-deco tower under a hazy sky"></div>

  <header class="top-bar">
    <div class="brand">PLENVORIA</div>
    <nav class="auth">
      <a href="#">SIGN UP</a>
      <a href="#">LOGIN</a>
    </nav>
  </header>

  <ul class="main-menu">
    <li class="active"><span>ABOUT</span><span>&gt;&gt;</span></li>
    <li><span>FEATURES</span><span>&gt;&gt;</span></li>
    <li><span>PRICING</span><span>&gt;&gt;</span></li>
  </ul>

  <div class="tagline">
    <p>Making sense of your business.</p>
    <p>Discover power of visual<br>industry ecosystem.</p>
  </div>

  <footer class="site-footer">
    <svg class="social" width="1200" height="63" viewBox="0 0 1200 63" aria-label="Social links">
      <g fill="none" stroke="#ffffff" stroke-width="2">
        <circle cx="533" cy="30" r="15"/>
        <circle cx="578" cy="30" r="15"/>
        <circle cx="622" cy="30" r="15"/>
        <circle cx="665" cy="30" r="15"/>
      </g>
    </svg>
  </footer>
</body>
</html>
```